Thimble Nook web site

I have been running an online business for 6 years.
www.thimblenook.com.au I specialise in ribbons, buttons and unique craft materials. I sell online to individuals and shops with seperate retail and wholesale sites. The web page I'd like redesigned is my retail site.

It needs a clean, fresh look. I've recently had a new logo designed (thanks pixel harbour!) and want the web site to incorporate the new design and colour scheme of black and white. (new logo attached as a file)

I no longer want the page with the large image www.thimblenook.com.au I want to have the first page as the retail shop homepage.
http://www.thimblenook.com.au/index.php so this page needs to have all the links

I want to the look to be fresh, modern and clear. It needs to be quick to load.

Notes from my IT guru: They need to know that the following tend to remain static with just the content section changing on each page; Header Left column (but different in the cart) right column (if required) footer
Updates

Thanks for your designs. 1/3 of my users use mobile devices so please take that into consideration. I would like the logo to be incorporated into the design and be a prominent feature (most have just used it as a tiny image in the top left corner. I would like it to be larger and more prominent.  thanks                                   

Thanks to all the designers who have submitted. Can you please add  'Boutique craft supplies' near the logo. That is my tag line. Thanks

Target Market(s)

Crafty females of all ages

Industry/Entity Type

Business

Requirements
Must have
• links to;
blog
gallery
chatterloop
snapboardly
wholesale
space for an image which I change approx every 2 weeks
about Thimble Nook
contact
privacy policy
terms and conditions
newsletter sign up
shipping info
product search
Nice to have
• I am not sure if I want product images on the homepage? I have attached a few images.
Should not have
• not too much colour - I hate the green border I have now

```html
<!DOCTYPE html>
<html lang="en">
<head>
<meta charset="utf-8">
<title>Thimble Nook – Boutique craft supplies</title>
<link href="https://fonts.googleapis.com/css2?family=Roboto:wght@300;400;500&display=swap" rel="stylesheet">
<style>
:root{
  --ink:#111;
  --text:#333;
  --muted:#666;
  --line:#d6d6d6;
  --accent:#35a9e0;
  --accent-dark:#2a95c8;
  --band-top:#f7f7f7;
  --band-bottom:#e2e2e2;
  --price-band:#e6e6e6;
  --white:#fff;
}
*{box-sizing:border-box;margin:0;padding:0}
html,body{width:1034px;height:1200px;overflow:hidden;background:var(--white)}
body{font-family:"Roboto",Arial,sans-serif;color:var(--text)}
.page{position:relative;width:1000px;height:1160px;transform:scale(1.034);transform-origin:0 0}
.abs{position:absolute}

/* header */
.nav-band{left:0;top:70px;width:1000px;height:32px;background:linear-gradient(var(--band-top),var(--band-bottom));border-top:1px solid var(--line);border-bottom:1px solid var(--line)}
.brand{left:135px;top:62px;width:185px;display:flex;align-items:center;gap:10px}
.brand-dot{width:30px;height:30px;border-radius:50%;background:var(--ink);flex:none}
.brand-name{font-size:23px;font-weight:400;color:var(--ink);white-space:nowrap}
.search{left:340px;top:36px;width:215px;height:17px;display:flex}
.search-field{flex:1;border:1px solid #bbb;font-size:10px;color:#888;padding:2px 3px;line-height:11px}
.search-btn{width:21px;background:var(--ink);display:flex;align-items:center;justify-content:center}
.phone{left:648px;top:36px;display:flex;align-items:center;gap:6px;font-size:14px;color:var(--ink)}
.cart{left:764px;top:36px;display:flex;align-items:center;gap:7px;font-size:11px;color:var(--ink);font-weight:500}
.cart-total{color:var(--accent);font-size:13px;font-weight:300}
.main-nav{left:340px;top:70px;height:32px;display:flex;list-style:none}
.main-nav li{font-size:12px;color:var(--ink);display:flex;align-items:center;justify-content:center;border-right:1px solid #cfcfcf;height:32px}
.main-nav li.is-active{background:var(--accent);color:var(--white)}

/* intro */
.tagline{left:340px;top:113px;font-size:18px;font-weight:400;color:var(--ink)}
.event-note{left:340px;top:137px;font-size:11px;color:var(--muted);font-weight:300}
.hero{left:340px;top:163px;width:525px;height:281px;border:1px solid #555;background:linear-gradient(160deg,#c9e3d2 0%,#e9d9f0 30%,#b9a3de 48%,#f1c9d6 66%,#f3e59a 84%,#f5f5f5 100%)}
.slider-dots{left:340px;top:457px;display:flex;gap:5px}
.slider-dots span{width:7px;height:7px;background:#ddd}
.slider-dots span.is-current{background:var(--ink)}

/* categories */
.section-bar{left:340px;top:483px;width:525px;height:30px;border:1px solid var(--line);background:linear-gradient(var(--white),#e6e6e6);padding-left:16px;font-size:17px;font-weight:300;color:var(--ink);line-height:28px}
.section-bar strong{font-weight:400}
.card{width:146px;height:246px;border:1px solid #cfcfcf;background:var(--white);text-align:center}
.card-image{margin:10px auto 0;width:114px;height:120px;border:1px solid #ccc}
.card-title{margin-top:9px;font-size:13px;color:var(--ink)}
.card-sub{font-size:11px;color:var(--muted);font-weight:300}
.card-price{margin-top:5px;height:26px;background:var(--price-band);font-size:14px;color:var(--ink);line-height:26px}
.btn{display:inline-block;background:var(--accent);color:var(--white);font-size:10px;text-transform:uppercase;line-height:22px}
.card .btn{margin-top:11px;width:101px}
.row-divider{left:340px;top:803px;width:525px;border-top:1px dashed #bbb}

/* sidebar */
.category-list{left:133px;top:165px;width:187px;list-style:none}
.category-list li{height:26.4px;border-top:1px dotted #bbb;font-size:11px;color:#444;display:flex;align-items:center;padding-left:10px;gap:10px}
.category-list li.is-active{background:linear-gradient(#ececec,#dcdcdc);color:var(--ink);border-top:1px solid #ccc}
.widget-head{left:134px;width:186px;height:27px;background:var(--ink);color:var(--white);font-size:14px;font-weight:300;padding-left:6px;line-height:27px}
.newsletter-copy{left:140px;top:854px;font-size:11px;color:var(--ink)}
.field{left:141px;width:171px;height:19px;border:1px solid #ccc;background:#f4f4f4;font-size:10px;color:#999;padding:3px 6px}
.join{left:141px;top:946px;width:44px;text-align:center;font-weight:500}
.social{top:1028px;width:100px;text-align:center;font-size:10px;color:#222}
.social-dot{width:30px;height:30px;border-radius:50%;background:#444;margin:0 auto 11px}
.social-divider{left:222px;top:1024px;height:54px;border-left:1px solid var(--line)}

/* footer */
.footer{left:5px;top:1107px;width:995px;height:53px;background:linear-gradient(#fafafa,#e4e4e4);border-top:1px solid var(--line);border-left:1px solid #ccc;text-align:center}
.footer-nav{margin-top:13px;font-size:10.5px;color:#222;display:flex;justify-content:center;list-style:none}
.footer-nav li+li::before{content:"|";margin:0 9px;color:#555}
.footer-nav .is-active{color:var(--accent);text-decoration:underline}
.copyright{margin-top:4px;font-size:10.5px;color:#222}
.copyright strong{font-weight:500}
</style>
</head>
<body>
<div class="page">

  <div class="abs nav-band"></div>

  <div class="abs brand">
    <span class="brand-dot"></span>
    <span class="brand-name">Thimble Nook</span>
  </div>

  <div class="abs search">
    <div class="search-field">Search Thimble Nook ...</div>
    <div class="search-btn">
      <svg width="11" height="11" viewBox="0 0 11 11"><circle cx="4.5" cy="4.5" r="3.3" fill="none" stroke="#fff" stroke-width="1.6"/><line x1="7" y1="7" x2="10" y2="10" stroke="#fff" stroke-width="1.8"/></svg>
    </div>
  </div>

  <div class="abs phone">
    <svg width="10" height="16" viewBox="0 0 10 16"><path d="M4 1 C1 3 1 13 4 15 L6 13 C4.5 11 4.5 5 6 3 Z" fill="#bbb"/></svg>
    512 367 904
  </div>

  <div class="abs cart">
    <svg width="19" height="15" viewBox="0 0 19 15"><path d="M1 1 H4 L6 10 H16 L18 4 H5" fill="none" stroke="#aaa" stroke-width="1.3"/><circle cx="7" cy="13" r="1.3" fill="#aaa"/><circle cx="15" cy="13" r="1.3" fill="#aaa"/></svg>
    <span>MY CART - <span class="cart-total">0.00</span></span>
  </div>

  <ul class="abs main-nav">
    <li class="is-active" style="width:68px">Home</li>
    <li style="width:93px">Shop</li>
    <li style="width:98px">Wholesale</li>
    <li style="width:93px">Gallery</li>
    <li style="width:75px">Blog</li>
    <li style="width:98px">Contact</li>
  </ul>

  <h1 class="abs tagline">Boutique craft supplies</h1>
  <p class="abs event-note">Harbourside Craft &amp; Quilt Fair 22-26th May, Riverbend Exhibition Hall. STAND G32</p>

  <div class="abs hero" role="img" aria-label="Feature image: bundle of pastel gingham ribbons"></div>
  <div class="abs slider-dots"><span class="is-current"></span><span></span><span></span><span></span><span></span><span></span><span></span><span></span><span></span></div>

  <h2 class="abs section-bar"><strong>Latest</strong> Categories</h2>

  <div class="abs card" style="left:340px;top:533px">
    <div class="card-image" role="img" aria-label="Stack of patterned washi tape rolls" style="background:linear-gradient(#8a9a5a,#e6b64a 40%,#d98a5a 70%,#f0a060)"></div>
    <div class="card-title">Transport ribbon</div><div class="card-sub">car, helicopter and truck</div>
    <div class="card-price">$ 2.50 only</div><span class="btn">View Products</span>
  </div>
  <div class="abs card" style="left:529px;top:533px">
    <div class="card-image" role="img" aria-label="Stack of patterned washi tape rolls" style="background:linear-gradient(#8a9a5a,#e6b64a 40%,#d98a5a 70%,#f0a060)"></div>
    <div class="card-title">Transport ribbon</div><div class="card-sub">car, helicopter and truck</div>
    <div class="card-price">$ 2.50 only</div><span class="btn">View Products</span>
  </div>
  <div class="abs card" style="left:719px;top:533px">
    <div class="card-image" role="img" aria-label="Pink and green fabric ribbon flowers" style="background:linear-gradient(120deg,#c9a0a8,#e8e4e0 50%,#a8c690)"></div>
    <div class="card-title">Transport ribbon</div><div class="card-sub">car, helicopter and truck</div>
    <div class="card-price">$ 2.50 only</div><span class="btn">View Products</span>
  </div>

  <div class="abs row-divider"></div>

  <div class="abs card" style="left:340px;top:828px">
    <div class="card-image" role="img" aria-label="Burgundy fabric ribbon flowers" style="background:linear-gradient(140deg,#f2f0f0,#9c3040 50%,#c49aa4)"></div>
    <div class="card-title">Transport ribbon</div><div class="card-sub">car, helicopter and truck</div>
    <div class="card-price">$ 2.50 only</div><span class="btn">View Products</span>
  </div>
  <div class="abs card" style="left:529px;top:828px">
    <div class="card-image" role="img" aria-label="Pastel gingham ribbons" style="background:linear-gradient(160deg,#d7eecf,#b9a3de 40%,#f1c9d6 65%,#f3e59a)"></div>
    <div class="card-title">Transport ribbon</div><div class="card-sub">car, helicopter and truck</div>
    <div class="card-price">$ 2.50 only</div><span class="btn">View Products</span>
  </div>
  <div class="abs card" style="left:719px;top:828px">
    <div class="card-image" role="img" aria-label="Rolls of striped and plain ribbon" style="background:linear-gradient(110deg,#c85060,#d8d0a0 50%,#a8c8a0 70%,#b0c8d8)"></div>
    <div class="card-title">Transport ribbon</div><div class="card-sub">car, helicopter and truck</div>
    <div class="card-price">$ 2.50 only</div><span class="btn">View Products</span>
  </div>

  <ul class="abs category-list">
    <li class="is-active">»&nbsp; New Products</li>
    <li>»&nbsp; ** Clearance **</li>
    <li>»&nbsp; Adhesives</li>
    <li>»&nbsp; Buttons</li>
    <li>»&nbsp; Card Kits</li>
    <li>»&nbsp; Charms</li>
    <li>»&nbsp; Chipboard</li>
    <li>»&nbsp; Christmas</li>
    <li>»&nbsp; Embellishments</li>
    <li>»&nbsp; Embossing Folders</li>
    <li>»&nbsp; Flowers and Leaves</li>
    <li>»&nbsp; inks, mists and masks</li>
    <li>»&nbsp; Lace</li>
    <li>»&nbsp; Miscellaneous</li>
    <li>»&nbsp; Paper</li>
    <li>»&nbsp; Punches</li>
    <li>»&nbsp; Ribbon Club</li>
    <li>»&nbsp; Ribbons</li>
    <li>»&nbsp; Ribbons - organza</li>
    <li>»&nbsp; Ric Rac</li>
    <li>»&nbsp; Sequins</li>
    <li>»&nbsp; Stamps</li>
    <li>»&nbsp; Stickers</li>
    <li>»&nbsp; Washi tape</li>
  </ul>

  <h3 class="abs widget-head" style="top:815px">News Letter</h3>
  <p class="abs newsletter-copy">Subscribe to our mailing list below:</p>
  <div class="abs field" style="top:881px">Enter your name ...</div>
  <div class="abs field" style="top:910px">Enter your Email ...</div>
  <span class="abs btn join">Join</span>

  <h3 class="abs widget-head" style="top:990px">Follow Us</h3>
  <div class="abs social" style="left:121px"><div class="social-dot"></div>CHATTERLOOP</div>
  <div class="abs social-divider"></div>
  <div class="abs social" style="left:223px"><div class="social-dot"></div>SNAPBOARDLY</div>

  <footer class="abs footer">
    <ul class="footer-nav">
      <li><span class="is-active">Home</span></li>
      <li>Shop</li>
      <li>Wholesale</li>
      <li>Gallery</li>
      <li>Blog</li>
      <li>About Thimble Nook</li>
      <li>Contact</li>
      <li>Privacy Policy</li>
      <li>Terms &amp; Conditions</li>
    </ul>
    <p class="copyright">Copyright © <strong>Thimble Nook</strong> 2013.All Right Reserved</p>
  </footer>

</div>
</body>
</html>
```